Nine Moons Brochure Design Project

I need a brochure for my new company "Nine Moons". You can read all about the company at http://www.ninemoons-example.com.sg
On the website you will also get an idea of the concept of the product, as well as design. This design actually comes from a Wordpress theme.
The brochure needs to be like a print version of the website but much more summarised, high-level. I'd like to distribute it to expecting mothers at various locations such as pre-natal yoga classes. The intention is to create enough interest so these moms-to-be will surf to my website and check out what it's all about.
Target Market(s)
Expecting moms and dads (pregnant)
Industry/Entity Type
It Company
Look and feel

```html
<!DOCTYPE html>
<html lang="en">
<head>
<meta charset="utf-8">
<title>Nine Moons – Brochure Spread</title>
<link rel="stylesheet" href="https://fonts.googleapis.com/css2?family=Ubuntu:wght@300;400;500;700&family=Comfortaa:wght@300;400&display=swap">
<style>
  :root {
    --paper: #f8f6f1;
    --paper-edge: #ecebe6;
    --brown: #8a4a1c;
    --brown-dark: #6e3a16;
    --ink: #2d2d2d;
    --logo-ink: #2f3a39;
    --band-top: #f4e4bb;
    --band-bottom: #e9d398;
    --ribbon: #b9b654;
    --ribbon-dark: #8c8a34;
    --ghost: #b7ab82;
  }
  * { margin: 0; padding: 0; box-sizing: border-box; }
  html, body { width: 1200px; height: 845px; overflow: hidden; background: #ffffff; }
  .spread {
    position: relative; width: 1200px; height: 845px; overflow: hidden;
    background: var(--paper);
    font-family: "Ubuntu", sans-serif;
  }
  .backdrop { position: absolute; inset: 0; }
  .photo { position: absolute; }
  .photo--mother {
    left: 0; top: 110px; width: 370px; height: 560px;
    background: radial-gradient(ellipse at 45% 45%, #e9ddd2 0%, #efe7df 45%, rgba(248,246,241,0) 75%);
  }
  .photo--bump {
    left: 600px; top: 282px; width: 320px; height: 380px;
    background: radial-gradient(ellipse at 40% 55%, #d9b9b8 0%, #e4cdcb 40%, rgba(248,246,241,0) 78%);
  }
  .photo--family {
    left: 650px; top: 705px; width: 220px; height: 140px;
    background: radial-gradient(ellipse at 50% 50%, #d8bf95 0%, rgba(236,216,160,0) 75%);
  }
  .text { position: absolute; white-space: nowrap; }
  .contact { left: 212px; width: 380px; text-align: center; color: var(--brown); font-weight: 300; font-size: 22px; }
  .contact__title { top: 66px; font-size: 38px; font-weight: 500; }
  .contact__web { top: 130px; }
  .contact__phone { top: 188px; }
  .contact__mail { top: 243px; line-height: 34px; }
  .quote { right: 619px; top: 556px; text-align: right; color: var(--brown); font-size: 29px; font-weight: 500; line-height: 44px; }
  .brand { font-family: "Ubuntu", sans-serif; font-weight: 500; color: var(--logo-ink); }
  .brand--header { left: 600px; width: 600px; top: 30px; text-align: center; font-size: 52px; }
  .brand--ghost { left: 100px; top: 732px; font-size: 60px; color: var(--ghost); opacity: .7; }
  .ribbon { position: absolute; left: 608px; top: 116px; width: 582px; height: 52px; }
  .ribbon__label { left: 600px; width: 600px; top: 127px; text-align: center; color: #fff; font-weight: 700; font-size: 14px; letter-spacing: .1px; }
  .headline { left: 600px; width: 610px; text-align: center; color: var(--brown); font-weight: 500; }
  .headline--congrats { top: 170px; font-size: 39px; }
  .headline--expecting { top: 217px; font-size: 48px; }
  .pitch { right: 25px; top: 327px; text-align: right; color: var(--ink); font-size: 20.5px; font-weight: 400; line-height: 31.8px; }
  .tagline { position: absolute; left: 600px; top: 620px; width: 600px; height: 100px; overflow: visible; }
  .tagline text { font-family: "Ubuntu", sans-serif; font-size: 20.5px; fill: var(--ink); }
  .signoff { right: 25px; text-align: right; font-family: "Comfortaa", sans-serif; color: var(--brown-dark); font-weight: 300; }
  .signoff__name { top: 712px; font-size: 34px; font-family: "Ubuntu", sans-serif; }
  .signoff__phone { top: 761px; font-size: 26px; color: var(--brown); }
  .signoff__web { top: 800px; font-size: 23px; color: var(--brown); }
</style>
</head>
<body>
<main class="spread">
  <svg class="backdrop" width="1200" height="845" viewBox="0 0 1200 845" aria-hidden="true">
    <defs>
      <linearGradient id="band" x1="0" y1="0" x2="0" y2="1">
        <stop offset="0" stop-color="var(--band-top)"/>
        <stop offset="1" stop-color="var(--band-bottom)"/>
      </linearGradient>
    </defs>
    <path d="M0 662 C 150 670, 400 690, 600 715 L 600 845 L 0 845 Z" fill="url(#band)"/>
    <path d="M600 705 C 800 700, 1050 675, 1200 640 L 1200 845 L 600 845 Z" fill="url(#band)"/>
    <path d="M0 640 C 150 665, 400 690, 600 715" fill="none" stroke="#ffffff" stroke-width="14" opacity=".9"/>
    <path d="M600 705 C 800 700, 1050 675, 1200 640" fill="none" stroke="#ffffff" stroke-width="14" opacity=".9"/>
    <line x1="600" y1="0" x2="600" y2="845" stroke="var(--paper-edge)" stroke-width="3"/>
    <line x1="602" y1="0" x2="602" y2="845" stroke="#ddd9d0" stroke-width="1"/>
  </svg>

  <div class="photo photo--mother" role="img" aria-label="Photo of a smiling pregnant woman resting on a bed while talking on the phone"></div>
  <div class="photo photo--bump" role="img" aria-label="Photo of a pair of tiny baby sneakers held above a pregnant belly"></div>
  <div class="photo photo--family" role="img" aria-label="Portrait photo of a mother with her baby"></div>

  <section class="panel panel--back">
    <p class="text contact contact__title">To know more:</p>
    <p class="text contact contact__web">Visit: www.ninemoons-example.com.sg</p>
    <p class="text contact contact__phone">Call Me at: 8123-4567</p>
    <p class="text contact contact__mail">Mail Me at:<br>clara@ninemoons-example.com.sg</p>
    <p class="text quote">Motherhood is a dream.<br>It really is absolutely amazing.</p>
    <p class="text brand brand--ghost">Nine Moons</p>
  </section>

  <section class="panel panel--front">
    <p class="text brand brand--header">Nine Moons</p>
    <svg class="ribbon" viewBox="0 0 582 52" aria-hidden="true">
      <path d="M0 30 L40 22 L40 44 L12 46 Z" fill="var(--ribbon)"/>
      <path d="M582 30 L542 22 L542 44 L570 46 Z" fill="var(--ribbon)"/>
      <path d="M40 44 L52 38 L52 44 Z" fill="var(--ribbon-dark)"/>
      <path d="M542 44 L530 38 L530 44 Z" fill="var(--ribbon-dark)"/>
      <rect x="40" y="4" width="502" height="34" fill="var(--ribbon)"/>
    </svg>
    <p class="text ribbon__label">PERSONALISED BABY PLANNER &amp; MATERNITY CONCIERGE</p>
    <h1 class="text headline headline--congrats">Congratulations,</h1>
    <h2 class="text headline headline--expecting">You’re expecting!</h2>
    <p class="text pitch">While endless joy awaits you<br>at the end of 40 weeks, a<br>mountain of tasks is slowly<br>but steadily piling up in<br>anticipation of your little one.<br>And questions, so many<br>questions that your<br>doctor/midwife just can’t<br>answer for you!</p>
    <svg class="tagline" viewBox="0 0 600 100">
      <path id="tagline-curve" d="M30 85 C 200 60, 420 75, 578 38" fill="none"/>
      <text><textPath href="#tagline-curve">From what to buy- to -planning the baby shower. Everything.</textPath></text>
    </svg>
    <p class="text signoff signoff__name">Clara Vermeulen</p>
    <p class="text signoff signoff__phone">Call - 8123-4567</p>
    <p class="text signoff signoff__web">or visit: ninemoons-example.com.sg</p>
  </section>
</main>
</body>
</html>
```